Venture Capital firm needs modern business cards

We are a Venture Capital firm within financial services/Asset management. The industry generally has basic business cards with black, blue and maybe green/yellow design elements.
Our firm has a four-colour swoosh logo. We are based in London and want to stand out, just a little bit!, from the crowd. Our company is called ROLK Investments and the 'C' stands for collaboration thus using artfolkhub is a natural portal for our business card design competition. Our logo came via artfolkhub too!
We use 'Venture Partner in Asset Management' as our tagline and this is Trademark registered. We operate in a conservative industry and we should not overstep our mark. The logo is colorful as it is and therefore the rest of the design should not be too fanciful.
The objective is twofold: make our logo element stick and memorable with our audience, whilst representing a conservative yet young image.
The Business Card obviously needs a field for Name, Surname, Job Title, Adress fields: Street, City, Postcode, Country, telefone and cell number, website address, etc.
We have uploaded the ai file. We trust that these are OK. If not, please advise.
Reason: We have have been busy with a client engagement. We will set the project as Guaranteed in return for the troubles we cause. Apologies for the confusion.
Thank you all for these great and creative design suggestions. The team is very happy with a number of your ideas! We will be in touch tomorrow to give individual feedback before the project closes on Friday. We look forward to working with some of you to narrow down your creations. Thank you, ROLK Investments team.
All,
Target Market(s)
Financial Services Professionals, Investors, Media, 35-70 years, mainly male, well educated
Industry/Entity Type
Conservative
Requirements
Must have
- We must make use of our logo and potential tagline 'Venture Partner in Asset Management' as we are establishing a new Brand and new company in the market.
We can use 'ROLK', 'ROLK Investments', and 'ROLK Investments'+tagline 'Venture Partner in Asset Management' or simply the four-colour swoosh plus the name of the company as part of the text. (see files)
All design elements are available in black or grey-scale if required. (grey scale swoosh attached).
Due to regulation we must have the following wording on the card in small print 'ROLK Investments is an Appointed Representative of Brambury Monetary Ventures Limited, which is authorised by the Pemberton Oversight Board'.
Nice to have
- We would consider designs that make use of different printing techniques such embossing/debossing, UV spot etc.
We attach our colour palette in the files section for your reference.
Should not have
- The font we use for our company name is 'EXO' so do not use a font style that clashes with the corporate fonts, please.
Do not use other design elements than the ones we provide in the file library as part of this project.

```html
<!DOCTYPE html>
<html lang="en">
<head>
<meta charset="utf-8">
<title>ROLK Investments – Business Cards</title>
<link rel="stylesheet" href="https://fonts.googleapis.com/css2?family=Exo:wght@400;500&family=Didact+Gothic&family=Questrial&display=swap">
<style>
  :root {
    --backdrop: #3b3b3b;
    --card: #ffffff;
    --ink: #333836;
    --ink-soft: #555a58;
    --band: #333836;
    --accent: #8cc63f;
  }
  * { box-sizing: border-box; margin: 0; padding: 0; }
  html, body {
    width: 1200px; height: 900px; overflow: hidden;
    background: var(--backdrop);
  }
  .canvas { position: relative; width: 1200px; height: 900px; }

  .card {
    position: absolute;
    width: 690px; height: 395px;
    background: var(--card);
    box-shadow: 0 10px 28px rgba(0,0,0,.45);
  }

  /* Front */
  .card--front { left: 60px; top: 45px; }
  .brand {
    position: absolute; left: 60px; top: 70px;
    display: flex; align-items: center; gap: 26px;
  }
  .brand__dot {
    width: 120px; height: 120px; border-radius: 50%;
    background: var(--accent);
  }
  .brand__name {
    font-family: "Exo", sans-serif; font-weight: 500;
    font-size: 190px; line-height: 1; color: var(--ink);
    letter-spacing: 2px;
  }
  .tagline {
    position: absolute; left: 266px; top: 262px;
    font-family: "Exo", sans-serif; font-weight: 400;
    font-size: 22px; color: var(--ink);
  }
  .small-print {
    position: absolute; left: 40px; right: 40px; bottom: 22px;
    font-family: "Didact Gothic", sans-serif;
    font-size: 9.5px; color: var(--ink-soft); text-align: center;
  }

  /* Back */
  .card--back { left: 450px; top: 470px; display: flex; }
  .card__band {
    width: 220px; height: 100%;
    background: var(--band);
    padding: 18px 20px;
  }
  .band__tile {
    width: 180px; height: 170px; border-radius: 10px;
    background: var(--card);
    display: flex; align-items: center; justify-content: center;
  }
  .band__name {
    font-family: "Exo", sans-serif; font-weight: 500;
    font-size: 46px; color: var(--ink);
  }
  .contact {
    flex: 1; padding: 34px 30px 0 36px;
    font-family: "Questrial", sans-serif; color: var(--ink);
  }
  .contact__name {
    font-family: "Didact Gothic", sans-serif;
    font-size: 72px; line-height: .95; font-weight: 400;
  }
  .contact__title { font-size: 22px; margin-bottom: 30px; }
  .contact__group { font-size: 15.5px; line-height: 1.3; margin-bottom: 18px; }
</style>
</head>
<body>
<main class="canvas">
  <section class="card card--front" aria-label="Business card front">
    <div class="brand">
      <span class="brand__dot" aria-hidden="true"></span>
      <span class="brand__name">rolk</span>
    </div>
    <p class="tagline">Venture Partner in Asset Management</p>
    <p class="small-print">ROLK Investments is an Appointed Representative of Brambury Monetary Ventures Limited, which is authorised by the Pemberton Oversight Board</p>
  </section>

  <section class="card card--back" aria-label="Business card back">
    <div class="card__band">
      <div class="band__tile"><span class="band__name">rolk</span></div>
    </div>
    <div class="contact">
      <h1 class="contact__name">Name</h1>
      <p class="contact__title">Job Title</p>
      <p class="contact__group">Phone: 845-xxx-xxxx<br>Cell: 845-xxx-xxxx</p>
      <p class="contact__group">E-mail: Example@example.com</p>
      <p class="contact__group">27 Placeholder Row, New York, NY<br>10001</p>
      <p class="contact__group">www.rolkinvestments.com</p>
    </div>
  </section>
</main>
</body>
</html>
```